" Consultório odontológico diferenciado, sou formado há 28 anos, em fase de instalação, pequeno, mas com todos os equipamentos necessários para realizar odontologia de alto nível. "

```html
<!DOCTYPE html>
<html lang="pt-BR">
<head>
<meta charset="utf-8">
<title>Papel timbrado – Lumen Odontologia</title>
<link href="https://fonts.googleapis.com/css2?family=Cinzel:wght@500&family=Montserrat:wght@400;500&display=swap" rel="stylesheet">
<style>
  :root {
    --backdrop: #e6e6e8;
    --paper: #ffffff;
    --ink: #4a4a4c;
    --ink-soft: #6d6d70;
    --gold-dark: #8a6d2c;
    --gold: #c9a95c;
    --gold-light: #f0dfa8;
    --rule: #9a9a9c;
    --watermark: #ececef;
  }
  * { margin: 0; padding: 0; box-sizing: border-box; }
  html, body {
    width: 1200px; height: 1200px; overflow: hidden;
    background: var(--backdrop);
  }
  .letterhead {
    position: absolute; left: 218px; top: 60px;
    width: 764px; height: 1080px;
    background: var(--paper);
    box-shadow: 0 4px 18px rgba(0,0,0,.12);
    font-family: "Montserrat", sans-serif;
    color: var(--ink);
  }
  .brand {
    position: absolute; left: 40px; top: 48px;
    display: flex; align-items: center; gap: 14px;
  }
  .brand-mark {
    width: 46px; height: 46px; border-radius: 50%;
    background: var(--gold);
  }
  .brand-text { display: flex; flex-direction: column; }
  .brand-name {
    font-family: "Cinzel", serif; font-weight: 500;
    font-size: 52px; line-height: 1; color: var(--ink);
    letter-spacing: 1px;
  }
  .brand-tagline {
    font-size: 11px; letter-spacing: 5px; text-transform: uppercase;
    color: var(--gold-dark); margin-top: 4px; text-align: center;
  }
  .website {
    position: absolute; right: 38px; top: 76px;
    font-size: 14px; letter-spacing: 3.5px; color: var(--ink-soft);
  }
  .edge-accent {
    position: absolute; right: 0; top: 64px;
    width: 8px; height: 48px;
    background: linear-gradient(180deg, var(--gold-light), var(--gold-dark));
  }
  .watermark {
    position: absolute; left: 90px; top: 180px;
    width: 600px; height: 620px;
    background: radial-gradient(ellipse at 45% 40%, var(--watermark) 0%, rgba(236,236,239,.5) 45%, rgba(255,255,255,0) 72%);
  }
  .signature-rule {
    position: absolute; left: 90px; right: 150px; top: 930px;
    height: 1px; background: var(--rule);
  }
  .contact {
    position: absolute; left: 0; right: 0; top: 962px;
    text-align: center; font-size: 12.5px; line-height: 22px; color: var(--ink-soft);
  }
  .contact .sep { margin: 0 10px; color: var(--rule); }
  .footer-band {
    position: absolute; left: 0; right: 0; top: 1030px; height: 30px;
    background: linear-gradient(90deg, var(--gold-dark) 0%, var(--gold) 25%, var(--gold-light) 50%, var(--gold) 75%, var(--gold-dark) 100%);
  }
</style>
</head>
<body>
  <main class="letterhead">
    <div class="watermark" role="img" aria-label="Faint large background emblem of the practice"></div>

    <header class="brand">
      <span class="brand-mark"></span>
      <div class="brand-text">
        <span class="brand-name">LUMEN</span>
        <span class="brand-tagline">Odontologia</span>
      </div>
    </header>

    <p class="website">lumenodontologia.com.br</p>
    <span class="edge-accent"></span>

    <div class="signature-rule"></div>

    <footer class="contact">
      <p>+55 11 4000-1234<span class="sep">|</span>contato@lumenodontologia.com.br</p>
      <p>R. das Acácias, 214 - Sala 12 - Jd. Aurora - CEP 04512-030 / São Paulo-SP</p>
    </footer>

    <div class="footer-band"></div>
  </main>
</body>
</html>
```